Zelvora - Creative Robotics

We are a software house for Audio Visual Systems integration/automation and home automation. we develop innovative software to automate a variety of devices mainly related to audio visuals and we design touch panel user interfaces to control these systems.

We would like to see designs that stick to our colours and theme, which you can find on our webpage www.zelvora-sample.com.au

The final design should communicate touch panels, innovation, software and automation.

Industry/Entity Type

Software

Requirements
Must have
• The business card must show the following information:
Name example : Derek Halvey
Qualification example: B Eng ICT(CompSys) Dip EngPrac
Title example : Control Systems Programmer
Mobile Phone, Company phone, Email address ,Company website

```html
<!DOCTYPE html>
<html lang="en">
<head>
<meta charset="utf-8">
<title>Zelvora – Business Cards</title>
<link rel="stylesheet" href="https://fonts.googleapis.com/css2?family=Arimo:wght@400;700&display=swap">
<style>
  :root {
    --blue: #1f72ba;
    --green: #029a52;
    --white: #ffffff;
    --ink: #2b2b2b;
    --page: #ffffff;
  }
  * { margin: 0; padding: 0; box-sizing: border-box; }
  html, body { width: 1037px; height: 1200px; overflow: hidden; background: var(--page); }
  .stage {
    position: relative; width: 1000px; height: 1157px;
    transform: scale(1.037); transform-origin: 0 0;
    font-family: "Arimo", Arial, sans-serif;
  }
  .card { position: absolute; width: 403px; height: 260px; }
  .card-front--blue-green { left: 78px; top: 277px; }
  .card-front--green-blue { left: 516px; top: 277px; }
  .card-back--blue { left: 75px; top: 620px; --accent: var(--blue); }
  .card-back--green { left: 516px; top: 620px; --accent: var(--green); }
  .card svg.backdrop { position: absolute; inset: 0; }

  .brand {
    position: absolute; left: 0; right: 0; top: 136px;
    display: flex; flex-direction: column; align-items: center;
  }
  .brand-row { display: flex; align-items: center; gap: 8px; }
  .brand-mark { width: 18px; height: 18px; background: var(--green); }
  .brand-name { font-weight: 700; font-size: 28px; color: var(--blue); letter-spacing: 0.5px; line-height: 1; }
  .brand-tagline { font-weight: 700; font-size: 6px; color: var(--blue); margin-top: 3px; margin-left: 26px; }

  .card-back { background: var(--accent); }
  .card-back .panel {
    position: absolute; left: 14px; top: 14px; right: 14px; bottom: 16px;
    background: var(--white); border-radius: 14px;
  }
  .gap-v { position: absolute; left: 192px; width: 10px; height: 14px; background: var(--white); }
  .gap-v.top { top: 0; } .gap-v.bottom { bottom: 0; height: 16px; }
  .gap-h { position: absolute; top: 127px; height: 10px; width: 14px; background: var(--white); }
  .gap-h.left { left: 0; } .gap-h.right { right: 0; }

  .details { position: absolute; left: 36px; top: 33px; list-style: none; }
  .details li {
    position: absolute; left: 0; display: flex; align-items: center;
    font-size: 15px; color: var(--ink); white-space: nowrap; height: 22px;
  }
  .details .icon { width: 24px; height: 22px; color: var(--accent); margin-right: 11px; display: flex; justify-content: center; align-items: center; }
  .details .icon svg { width: 22px; height: 20px; }
</style>
</head>
<body>
<main class="stage">

  <section class="card card-front--blue-green" aria-label="Card front, green and blue">
    <svg class="backdrop" viewBox="0 0 403 260" width="403" height="260">
      <rect width="403" height="260" fill="var(--green)"/>
      <path d="M0 260 L403 0 L403 260 Z" fill="var(--blue)"/>
      <path d="M0 260 C30 90 230 30 403 0 C370 130 220 230 0 260 Z" fill="var(--white)"/>
    </svg>
    <div class="brand">
      <div class="brand-row"><span class="brand-mark"></span><span class="brand-name">Zelvora</span></div>
      <span class="brand-tagline">Creative Robotics</span>
    </div>
  </section>

  <section class="card card-front--green-blue" aria-label="Card front, blue and green">
    <svg class="backdrop" viewBox="0 0 403 260" width="403" height="260">
      <rect width="403" height="260" fill="var(--blue)"/>
      <path d="M0 260 L403 0 L403 260 Z" fill="var(--green)"/>
      <path d="M0 260 C30 90 230 30 403 0 C370 130 220 230 0 260 Z" fill="var(--white)"/>
    </svg>
    <div class="brand">
      <div class="brand-row"><span class="brand-mark"></span><span class="brand-name">Zelvora</span></div>
      <span class="brand-tagline">Creative Robotics</span>
    </div>
  </section>

  <section class="card card-back card-back--blue" aria-label="Card back, blue">
    <div class="panel"></div>
    <span class="gap-v top"></span><span class="gap-v bottom"></span>
    <span class="gap-h left"></span><span class="gap-h right"></span>
    <ul class="details">
      <li style="top:0"><span class="icon"><svg viewBox="0 0 22 20"><circle cx="11" cy="5.5" r="4.5" fill="currentColor"/><path d="M3 20 C3 12 19 12 19 20 Z" fill="currentColor"/></svg></span>Derek Halvey</li>
      <li style="top:27px"><span class="icon"><svg viewBox="0 0 22 20"><rect x="2.5" y="1.5" width="17" height="17" fill="none" stroke="currentColor" stroke-width="2"/><path d="M6 10 L10 14 L16 5" fill="none" stroke="currentColor" stroke-width="2.4"/></svg></span>B Eng ICT (CompSys) Dip EngPrac</li>
      <li style="top:52px"><span class="icon"><svg viewBox="0 0 22 20"><rect x="1" y="3" width="20" height="14" fill="none" stroke="currentColor" stroke-width="1.6"/><circle cx="6.5" cy="8.5" r="2" fill="currentColor"/><path d="M3.5 14 C3.5 10.5 9.5 10.5 9.5 14 Z" fill="currentColor"/><path d="M11.5 7h7M11.5 10h7M11.5 13h7" stroke="currentColor" stroke-width="1.3"/></svg></span>Control Systems Programmer</li>
      <li style="top:84px"><span class="icon"><svg viewBox="0 0 22 20"><rect x="6" y="0" width="10" height="20" rx="2" fill="currentColor"/><rect x="7.5" y="2.5" width="7" height="13" fill="#cfe4f5"/></svg></span>481726053</li>
      <li style="top:113px"><span class="icon"><svg viewBox="0 0 22 20"><path d="M1 7 C1 2 21 2 21 7 L21 9 L16 9 L16 6 L6 6 L6 9 L1 9 Z" fill="currentColor"/><path d="M4 11 L7 8 L15 8 L18 11 L18 19 L4 19 Z" fill="currentColor"/><circle cx="11" cy="13.5" r="3" fill="#fff"/></svg></span>927305164</li>
      <li style="top:142px"><span class="icon"><svg viewBox="0 0 22 20"><text x="11" y="17" text-anchor="middle" font-family="Arimo, Arial, sans-serif" font-weight="700" font-size="20" fill="currentColor">@</text></svg></span>example@zelvora-mail.com</li>
      <li style="top:168px"><span class="icon"><svg viewBox="0 0 22 20"><circle cx="11" cy="10" r="9" fill="currentColor"/><path d="M6 4 C9 6 8 9 11 10 C9 13 12 15 10 18" fill="none" stroke="#fff" stroke-width="1.6"/></svg></span>www.example.com</li>
    </ul>
  </section>

  <section class="card card-back card-back--green" aria-label="Card back, green">
    <div class="panel"></div>
    <span class="gap-v top"></span><span class="gap-v bottom"></span>
    <span class="gap-h left"></span><span class="gap-h right"></span>
    <ul class="details">
      <li style="top:0"><span class="icon"><svg viewBox="0 0 22 20"><circle cx="11" cy="5.5" r="4.5" fill="currentColor"/><path d="M3 20 C3 12 19 12 19 20 Z" fill="currentColor"/></svg></span>Derek Halvey</li>
      <li style="top:27px"><span class="icon"><svg viewBox="0 0 22 20"><rect x="2.5" y="1.5" width="17" height="17" fill="none" stroke="currentColor" stroke-width="2"/><path d="M6 10 L10 14 L16 5" fill="none" stroke="currentColor" stroke-width="2.4"/></svg></span>B Eng ICT (CompSys) Dip EngPrac</li>
      <li style="top:52px"><span class="icon"><svg viewBox="0 0 22 20"><rect x="1" y="3" width="20" height="14" fill="none" stroke="currentColor" stroke-width="1.6"/><circle cx="6.5" cy="8.5" r="2" fill="currentColor"/><path d="M3.5 14 C3.5 10.5 9.5 10.5 9.5 14 Z" fill="currentColor"/><path d="M11.5 7h7M11.5 10h7M11.5 13h7" stroke="currentColor" stroke-width="1.3"/></svg></span>Control Systems Programmer</li>
      <li style="top:84px"><span class="icon"><svg viewBox="0 0 22 20"><rect x="6" y="0" width="10" height="20" rx="2" fill="currentColor"/><rect x="7.5" y="2.5" width="7" height="13" fill="#d3efdf"/></svg></span>481726053</li>
      <li style="top:113px"><span class="icon"><svg viewBox="0 0 22 20"><path d="M1 7 C1 2 21 2 21 7 L21 9 L16 9 L16 6 L6 6 L6 9 L1 9 Z" fill="currentColor"/><path d="M4 11 L7 8 L15 8 L18 11 L18 19 L4 19 Z" fill="currentColor"/><circle cx="11" cy="13.5" r="3" fill="#fff"/></svg></span>927305164</li>
      <li style="top:142px"><span class="icon"><svg viewBox="0 0 22 20"><text x="11" y="17" text-anchor="middle" font-family="Arimo, Arial, sans-serif" font-weight="700" font-size="20" fill="currentColor">@</text></svg></span>Example@zelvora-mail.com</li>
      <li style="top:168px"><span class="icon"><svg viewBox="0 0 22 20"><circle cx="11" cy="10" r="9" fill="currentColor"/><path d="M6 4 C9 6 8 9 11 10 C9 13 12 15 10 18" fill="none" stroke="#fff" stroke-width="1.6"/></svg></span>www.example.com</li>
    </ul>
  </section>

</main>
</body>
</html>
```